Craftwell Hub (Toronto) - Training Our Millenials

This website is going to be a trades and learning platform where you can sign-up and register for different trades that may suit your interests. With this site I want people to be able to pull up an on-line application form with a submit button to register on-line. I would also like to see this website include interactive images with links or landing pages to the trade or service they will be registering for. I would like it to be friendly and straightforward to anyone trying to apply. Since this program will originate in Toronto, Ontario Canada, I would also like that to be reflected in the web design(Pellmont Spire, Red Maple Leaf etc.) The following trades learning platforms will be included in my services and would like that to be reflected by 2-3 roll-over images for each trade profession:
-ELECTRICAL
-MECHANICAL
-PLUMBING
-CONTRACTORS
-FLOORING
-DRY-WALL
-ROOFING
-HANDY-MAN
-CARPENTRY
-MAINTENANCE
**REFER TO THIS WEBSITE FOR TEMPLATE OF IDEA
http://www.vireskillworks.example/anvilcrew/training.html
Target Market(s)
Employers, Youth, Adults, Un-Employed, Agencies
Industry/Entity Type
Trade
Coding
Coded - Design and coding required
Number of Pages Required
1 page
Requirements
Must have
- Must have images supporting each profession/trade, must include register on-line function, must include user friendly icons and themes, must represent Toronto, Canada in the web design. Must be a modern design with a professional feel.
Nice to have
- on-line support function where the admin user can communicate with individuals interested in asking questions or concerns.
Should not have
- should not be dull

```html
<!DOCTYPE html>
<html lang="en">
<head>
<meta charset="utf-8">
<title>Craftwell Hub – Skilled Trades Training</title>
<link rel="stylesheet" href="https://fonts.googleapis.com/css2?family=Oswald:wght@400;500&family=Open+Sans:ital,wght@0,400;0,600;0,700;1,700&display=swap">
<style>
:root{
  --orange:#f15a24;
  --black:#0d0d0d;
  --header:#141414;
  --dark:#1b1b1b;
  --footer:#1a1a1a;
  --footer-deep:#111;
  --light:#f4f4f4;
  --text:#555;
  --heading:#222;
  --sky:#0bb3e2;
  --white:#fff;
}
*{box-sizing:border-box;margin:0;padding:0}
html,body{width:1200px;height:2695px;overflow:hidden}
body{font-family:"Open Sans",Arial,sans-serif;color:var(--text);background:var(--white);position:relative}
.abs{position:absolute}
.oswald{font-family:"Oswald",Arial,sans-serif}

/* top bar */
.topbar{top:0;left:0;width:1200px;height:27px;background:var(--black);font-size:10px;color:#ddd}
.topbar .links{left:169px;top:7px;display:flex;gap:16px}
.topbar .account{left:823px;top:7px;display:flex;gap:16px;color:var(--orange);font-weight:600}
.topbar .social{left:915px;top:6px;display:flex;gap:14px}
.topbar .social span{width:14px;height:14px;border-radius:50%;border:1px solid #777;display:block}

/* header */
.header{top:27px;left:0;width:1200px;height:111px;background:rgba(20,20,20,.92);z-index:2}
.brand{left:200px;top:20px;display:flex;align-items:center;gap:12px}
.brand .dot{width:70px;height:70px;border-radius:50%;border:3px solid var(--orange);background:#2a2a2a}
.brand .name{font-family:"Oswald",Arial,sans-serif;font-size:22px;color:var(--white);font-weight:500;letter-spacing:1px}
.info{top:40px;display:flex;align-items:center;gap:10px;color:var(--white);font-size:10px}
.info svg{flex:none}
.info .txt{border-left:1px solid #555;padding-left:10px;line-height:15px}
.info b{font-family:"Oswald",Arial,sans-serif;font-weight:500;font-size:12px;display:block}
.info small{font-size:10px;color:#ccc}

/* nav */
.nav{top:138px;left:264px;width:670px;height:43px;background:var(--white);display:flex;z-index:3;font-family:"Oswald",Arial,sans-serif;font-size:11px;color:#222}
.nav a{display:flex;align-items:center;padding:0 17px;text-decoration:none;color:inherit;letter-spacing:.3px}
.nav .home{background:var(--orange);width:52px;justify-content:center;padding:0}
.nav .quote{background:var(--orange);color:var(--white);margin-left:auto;padding:0 20px;gap:6px}

/* hero */
.hero{top:27px;left:0;width:1200px;height:515px;background:linear-gradient(110deg,#201a15 0%,#3a2e24 45%,#4b3a2a 70%,#2a2420 100%)}
.hero-worker{top:130px;left:700px;width:330px;height:412px;background:linear-gradient(180deg,#d9a31a 0%,#6a4a33 35%,#3a2c24 100%);border-radius:120px 120px 0 0}
.hero-title{top:230px;left:169px;background:var(--orange);color:var(--white);font-family:"Oswald",Arial,sans-serif;font-size:31px;padding:2px 10px;line-height:42px}
.hero-sub{top:279px;left:169px;background:#555;color:var(--white);font-family:"Oswald",Arial,sans-serif;font-size:17px;padding:0 10px;line-height:31px;letter-spacing:.5px}
.hero-text{top:332px;left:169px;width:340px;font-size:10px;color:#eee;line-height:18px}
.btn{background:var(--orange);color:var(--white);font-size:10px;display:inline-flex;align-items:center;justify-content:center}
.hero-btn{top:406px;left:169px;width:80px;height:26px}
.arrow{top:282px}

/* services */
.services{top:542px;left:0;width:1200px;height:189px;background:linear-gradient(180deg,#3b2a18 0%,#6b4a24 40%,#1d2a4a 100%)}
.sec-title{width:1200px;text-align:center;color:var(--white);font-family:"Oswald",Arial,sans-serif;font-size:18px;letter-spacing:.5px}
.sec-sub{width:1200px;text-align:center;color:#eee;font-size:10px}
.filters{top:683px;left:77px;width:1040px;display:flex;justify-content:space-between;align-items:center;font-size:11px;color:var(--white)}
.filters span{padding:3px 6px}
.filters .active{background:var(--orange)}

.grid{top:731px;left:0;width:1200px;height:409px;display:grid;grid-template-columns:repeat(4,1fr);grid-template-rows:repeat(2,1fr);gap:2px;background:#fff}
.tile{width:100%;height:100%}
.t1{background:linear-gradient(160deg,#9fb3c6,#5a4a3a)}
.t2{background:linear-gradient(160deg,#d9c9a0,#8a7a5a)}
.t3{background:linear-gradient(160deg,#e8e8e8,#8a9ab0)}
.t4{background:linear-gradient(160deg,#c8d4e4,#3a3f4a)}
.t5{background:linear-gradient(160deg,#9ab4d8,#2a2f3a)}
.t6{background:linear-gradient(160deg,#c8bda8,#5a5a3a)}
.t7{background:linear-gradient(160deg,#f0f0f0,#8aa0b8)}
.t8{background:linear-gradient(160deg,#e4e8ee,#b08a70)}

.viewall{top:1140px;left:0;width:1200px;height:106px;background:linear-gradient(90deg,#2a2018,#5a4028,#2a2018)}
.viewall-btn{top:1171px;left:535px;width:131px;height:29px;gap:6px}

/* about */
.about{top:1246px;left:0;width:1200px;height:356px;background:var(--light)}
.heading{font-family:"Oswald",Arial,sans-serif;font-size:17px;color:var(--heading);border-left:3px solid var(--orange);padding-left:9px;line-height:18px;letter-spacing:.3px}
.about .heading{top:1289px;left:169px}
.about-copy{top:1328px;left:169px;width:864px;font-size:10px;line-height:16px;color:#666}
.about-copy p{margin-bottom:8px}

/* maple band */
.maple{top:1602px;left:0;width:1200px;height:321px;background:linear-gradient(135deg,#c8643a 0%,#e07a40 35%,#a84a2a 65%,#d8704a 100%)}
.maple-title{top:1650px;left:150px;width:900px;text-align:center;color:var(--white);font-family:"Oswald",Arial,sans-serif;font-size:17px;line-height:26px;letter-spacing:.3px}
.maple-sub{top:1712px;left:390px;width:420px;text-align:center;color:#fff;font-size:10px;line-height:18px}
.counter{top:1790px;width:198px;height:85px;background:rgba(255,255,255,.2);color:var(--white);text-align:center;padding-top:16px}
.counter .num{font-family:"Oswald",Arial,sans-serif;font-size:20px;display:flex;justify-content:center;align-items:center;gap:8px}
.counter .lbl{font-size:11px;text-transform:uppercase;margin-top:2px;color:#fff}

/* testimonial & why */
.testimonial-h{top:1947px;left:169px}
.why-h{top:1947px;left:611px}
.quote-box{top:1985px;left:169px;width:418px;height:145px;background:var(--white);box-shadow:0 0 6px rgba(0,0,0,.15)}
.quote-mark{top:1998px;left:186px;color:var(--orange);font-size:54px;font-family:Georgia,serif;font-weight:700;line-height:1}
.quote-text{top:2010px;left:249px;width:320px;font-size:13px;font-style:italic;font-weight:700;color:#333;line-height:23px}
.quote-author{top:2094px;left:249px;font-size:10px;color:#666;display:flex;align-items:center;gap:10px}
.quote-author i{width:18px;height:1px;background:var(--orange);display:block}
.quote-author b{color:#2a6fb5;font-weight:400}
.quote-dots{top:2098px;left:520px;display:flex;gap:3px}
.quote-dots span{width:8px;height:8px;background:var(--orange)}
.why-copy{top:1985px;left:611px;width:420px;font-size:10px;line-height:17px;color:#555}
.why-copy p{margin-bottom:8px}

/* tweet band */
.tweets{top:2179px;left:0;width:1200px;height:188px;background:var(--sky)}
.tw-circle{top:2209px;left:487px;width:54px;height:54px;border-radius:50%;background:var(--white)}
.tw-line{top:2236px;left:541px;width:116px;height:1px;background:rgba(255,255,255,.7)}
.tw-pill{top:2227px;left:557px;width:84px;height:18px;border-radius:9px;background:rgba(255,255,255,.3);color:var(--white);font-size:8px;display:flex;align-items:center;justify-content:center}
.tw-avatar{top:2209px;left:657px;width:54px;height:54px;border-radius:50%;background:linear-gradient(180deg,#e8eef2,#9ab0c0);border:2px solid var(--white)}
.tw-text{top:2278px;left:150px;width:900px;text-align:center;color:var(--white);font-size:18px;line-height:29px}

/* footer */
.footer{top:2367px;left:0;width:1200px;height:328px;background:var(--footer)}
.f-h{font-family:"Oswald",Arial,sans-serif;font-size:13px;color:var(--white);border-left:2px solid var(--orange);padding-left:8px;line-height:13px;top:2406px;letter-spacing:.3px}
.f-contact{top:2437px;left:169px;width:200px;font-size:9.5px;color:#ccc;line-height:15px}
.f-contact li{list-style:none;display:flex;gap:12px;margin-bottom:10px}
.f-contact svg{flex:none;margin-top:2px}
.f-posts{top:2437px;left:390px;width:200px;font-size:9.5px;color:#ccc}
.f-posts li{list-style:none;display:flex;justify-content:space-between;border-bottom:1px solid #333;padding:7px 0 7px 0}
.f-posts li span:first-child::before{content:"";display:inline-block;width:5px;height:5px;background:#ccc;margin-right:10px;vertical-align:middle}
.f-photos{top:2437px;left:611px;width:201px;display:grid;grid-template-columns:repeat(3,63px);gap:6px}
.f-photos div{height:62px;border:2px solid #eee}
.p1{background:linear-gradient(135deg,#d8d0c0,#7a6a5a)}
.p2{background:linear-gradient(135deg,#c0c8d8,#5a6070)}
.p3{background:linear-gradient(135deg,#e0c870,#6a5a40)}
.p4{background:linear-gradient(135deg,#8aa8c8,#2a3040)}
.p5{background:linear-gradient(135deg,#e0b030,#3a3a4a)}
.p6{background:linear-gradient(135deg,#e8e0c0,#8a7a5a)}
.f-form{top:2437px;left:832px;width:200px}
.f-form .field{height:26px;background:#2a2a2a;border:1px solid #333;margin-bottom:9px;font-size:9px;color:#aaa;padding:7px 8px}
.f-form .msg{height:50px}
.f-form .btn{width:100px;height:24px;font-size:8px;margin-top:4px}
.f-social{top:2627px;left:512px;display:flex;gap:8px}
.f-social span{width:22px;height:22px;display:block}
.f-bottom{top:2655px;left:0;width:1200px;height:40px;background:var(--footer-deep)}
.copyright{top:2664px;left:169px;font-size:9px;color:#aaa}
.totop{top:2660px;left:1003px;width:26px;height:24px;background:#222;display:flex;align-items:center;justify-content:center}
</style>
</head>
<body>

<!-- top bar -->
<div class="topbar abs">
  <div class="links abs"><span>About</span><span>Services</span><span>Terms &amp; Condition</span><span>Online Booking</span><span>Contact Us</span></div>
  <div class="account abs"><span>Signup</span><span>Login</span></div>
  <div class="social abs"><span></span><span></span><span></span><span></span><span></span></div>
</div>

<!-- hero -->
<div class="hero abs" role="img" aria-label="Dusky city construction site backdrop"></div>
<div class="hero-worker abs" role="img" aria-label="Construction worker in a hard hat handling building material"></div>

<!-- header -->
<header class="header abs">
  <div class="brand abs"><span class="dot"></span><span class="name">Craftwell Hub</span></div>
  <div class="info abs" style="left:630px">
    <svg width="16" height="16" viewBox="0 0 16 16"><circle cx="8" cy="8" r="6.5" fill="none" stroke="#f15a24" stroke-width="2"/><path d="M8 4.5V8l2.5 1.5" stroke="#f15a24" stroke-width="1.6" fill="none"/></svg>
    <div class="txt"><b>MONDAY - SUNDAY</b><small>8:00AM - 9:00PM</small></div>
  </div>
  <div class="info abs" style="left:795px">
    <svg width="16" height="16" viewBox="0 0 16 16"><path d="M3 1.5l3 .5 1 3.5-2 1.2a9 9 0 0 0 4.3 4.3l1.2-2 3.5 1 .5 3c-7 1-13-5-11.5-11.5z" fill="#f15a24"/></svg>
    <div class="txt"><b>CALL US NOW</b><small>+0458-555-01920</small></div>
  </div>
  <div class="info abs" style="left:937px">
    <svg width="14" height="18" viewBox="0 0 14 18"><path d="M7 0a6 6 0 0 0-6 6c0 4.5 6 12 6 12s6-7.5 6-12a6 6 0 0 0-6-6zm0 8.5A2.5 2.5 0 1 1 7 3.5a2.5 2.5 0 0 1 0 5z" fill="#f15a24"/></svg>
    <div class="txt"><b>LOCATION</b><small>SEE ON MAP</small></div>
  </div>
</header>

<nav class="nav abs">
  <a class="home"><svg width="16" height="14" viewBox="0 0 16 14"><path d="M8 0l8 7h-2.5v7h-4V9.5h-3V14h-4V7H0z" fill="#fff"/></svg></a>
  <a>ABOUT</a><a>SERVICES</a><a>BLOG</a><a>PORTFOLIO</a><a>TEAM</a><a>SHOP</a><a>CONTACT US</a>
  <a class="quote"><svg width="11" height="11" viewBox="0 0 11 11"><rect x="1" y="2" width="8" height="8" fill="none" stroke="#fff"/><path d="M5 6l5-5" stroke="#fff" stroke-width="1.4"/></svg>GET A QUOTE</a>
</nav>

<div class="hero-title abs">BUILDING MATERIAL</div>
<div class="hero-sub abs">LOREM IPSUM DOLLAR</div>
<p class="hero-text abs">Lorem Ipsum is simply dummy text of the printing and typesetting industry. Lorem Ipsum has been the industry's standard dummy text ever since the 1500s,</p>
<div class="hero-btn btn abs">Read More</div>
<svg class="arrow abs" style="left:18px" width="12" height="20" viewBox="0 0 12 20"><path d="M10 2L2 10l8 8" stroke="#ccc" stroke-width="2" fill="none"/></svg>
<svg class="arrow abs" style="left:1170px" width="12" height="20" viewBox="0 0 12 20"><path d="M2 2l8 8-8 8" stroke="#ccc" stroke-width="2" fill="none"/></svg>

<!-- services -->
<section class="services abs" role="img" aria-label="Toronto skyline and highway lights at night"></section>
<h2 class="sec-title abs" style="top:580px">OUR SERVICES</h2>
<p class="sec-sub abs" style="top:622px">Lorem Ipsum is simply dummy text of the is a printing and typesetting of a now get a1500s, is simply dummy text</p>
<div class="filters abs">
  <span class="active">All Projects</span><span>Buildings</span><span>Tiling</span><span>Interior Design</span><span>Electrical</span><span>Mechanical</span><span>Plumbing</span><span>Contractors</span><span>Flooring</span><span>Dry-wall</span><span>Roofing</span><span>Handy-Man</span><span>Carpentry</span><span>Maintenance</span>
</div>

<div class="grid abs">
  <div class="tile t1" role="img" aria-label="Worker in hard hat on a building site"></div>
  <div class="tile t2" role="img" aria-label="Drafting tools laid on blueprints"></div>
  <div class="tile t3" role="img" aria-label="Team of builders in white hard hats"></div>
  <div class="tile t4" role="img" aria-label="Contractors reviewing plans on a laptop"></div>
  <div class="tile t5" role="img" aria-label="Engineer with rolled plans on a steel bridge"></div>
  <div class="tile t6" role="img" aria-label="Tradesman holding a yellow hard hat"></div>
  <div class="tile t7" role="img" aria-label="Designer sketching technical plans at a desk"></div>
  <div class="tile t8" role="img" aria-label="Architect looking at a building model"></div>
</div>

<div class="viewall abs" role="img" aria-label="City street lights at dusk"></div>
<div class="viewall-btn btn abs">VIEW ALL PROJECTS <svg width="7" height="8" viewBox="0 0 7 8"><path d="M1 1l3 3-3 3M3.5 1l3 3-3 3" stroke="#fff" fill="none"/></svg></div>

<!-- about -->
<section class="about abs"></section>
<h2 class="heading abs about-h" style="top:1289px;left:169px">CRAFTWELL HUB - WHO WE ARE...</h2>
<div class="about-copy abs">
  <p>The Craftwell Hub Program is a twelve week skill and employment-based training program that links young men and women from under-resourced communities to apprenticeship career opportunities in the construction industry that they might otherwise have difficulty accessing.</p>
  <p>Participants are exposed to multiple construction trades over the course of the program. There is hands-on learning at various affiliate training centres located across the GTA in addition to jobsite visits. Participants are provided with leadership and mentoring from seasoned construction workers with years of work experience and learn valuable skill sets which build self-confidence and promote positive self-awareness.</p>
  <p>Craftwell Hub can link youth to twenty-eight different unions and the many major contractors connected to the Lakeshore Building Trades Council.</p>
  <p>Craftwell Hub Program is a skill and employment-based training program within the construction industry offering apprenticeship career opportunities to the youth of under-resourced neighbourhoods in our communities.</p>
  <p>Without this program these youths would not have access to the gainful employment opportunities that the unionized construction sector offers.</p>
  <p>The Lakeshore Building Trades Council has a history dating back to 1943. Currently, the LBTC represents over 80,000 skilled trades men and women in central Ontario.</p>
  <p>Get trained and get hired! Skilled Trades workers are in high demand. The Northgate Skills Institute's Skilled Trades Training Programs get students trained for rewarding careers in less than half the time of similar college training programs.</p>
</div>

<!-- maple band -->
<section class="maple abs" role="img" aria-label="Close-up of red and orange maple leaves"></section>
<h2 class="maple-title abs">LEADING THE WAY IN ELECTRICAL, MECHANICAL, PLUMBING, CONTRACTORS, FLOORING, DRY WALL, ROOFING, HANDY-MAN, CARPENTRY AND MAINTENANCE CONSTRUCTION</h2>
<p class="maple-sub abs">Lorem Ipsum is simply dummy text of the is a printing and typesetting of a now get a1500s, is simply dummy text</p>

<div class="counter abs" style="left:169px"><div class="num"><svg width="18" height="16" viewBox="0 0 16 14"><path d="M8 0l8 7h-2.5v7h-4V9.5h-3V14h-4V7H0z" fill="#f15a24"/></svg>1000</div><div class="lbl">Projects Completed</div></div>
<div class="counter abs" style="left:390px"><div class="num"><svg width="12" height="16" viewBox="0 0 12 16"><circle cx="6" cy="4" r="3.5" fill="#f15a24"/><path d="M0 16c0-5 2.5-7 6-7s6 2 6 7z" fill="#f15a24"/></svg>1015</div><div class="lbl">Workers Employed</div></div>
<div class="counter abs" style="left:611px"><div class="num"><svg width="14" height="16" viewBox="0 0 14 16"><circle cx="7" cy="6" r="5" fill="#f15a24"/><path d="M3.5 9.5L2 16l5-2 5 2-1.5-6.5z" fill="#f15a24"/></svg>10058</div><div class="lbl">Awards Won</div></div>
<div class="counter abs" style="left:832px"><div class="num"><svg width="14" height="16" viewBox="0 0 14 16"><path d="M7 0C2 5 1 9 3.5 12.5L7 16l3.5-3.5C13 9 12 5 7 0z" fill="#f15a24"/></svg>1015</div><div class="lbl">Green Construction</div></div>

<!-- testimonial & why -->
<h2 class="heading abs testimonial-h">TESTIMONIAL</h2>
<h2 class="heading abs why-h">WHY CHOOSE US?</h2>
<div class="quote-box abs"></div>
<div class="quote-mark abs">&ldquo;</div>
<p class="quote-text abs">Lorem Ipsum is simply dummy text of the is a printing and typesetting of a now get a1500s, is simply dummy text Lorem Ipsum is simply dummy</p>
<div class="quote-author abs"><i></i><span>Evan <b>Hollis</b></span></div>
<div class="quote-dots abs"><span></span><span></span><span></span></div>
<div class="why-copy abs">
  <p>Shorter programs with over 70% hands-on training gets students workforce ready earlier than most other programs.</p>
  <p>Over 17,000 square feet of fully-equipped shop space provides students with a full-scale experience.</p>
  <p>Students are trained by experienced instructors who work in the field and know the industry.</p>
</div>

<!-- tweet band -->
<section class="tweets abs"></section>
<div class="tw-line abs"></div>
<div class="tw-circle abs"></div>
<div class="tw-pill abs">@ALDENMORE</div>
<div class="tw-avatar abs" role="img" aria-label="Profile photo of the account holder"></div>
<p class="tw-text abs">@Marketbay if yes, send us an email via: http://lnk.example/k8Qm2Rz and let me know the email you registered with, i'll check the account</p>

<!-- footer -->
<footer class="footer abs"></footer>
<h3 class="f-h abs" style="left:169px">CONTACT INFO</h3>
<h3 class="f-h abs" style="left:390px">RECENT POSTS</h3>
<h3 class="f-h abs" style="left:611px">OUR PHOTOS</h3>
<h3 class="f-h abs" style="left:832px">QUICK INQUIRY</h3>

<ul class="f-contact abs">
  <li><svg width="12" height="12" viewBox="0 0 12 12"><path d="M6 0l6 3H0zM1 4h10v1H1zM2 5.5h1.5v4H2zm3.2 0h1.5v4H5.2zm3.3 0H10v4H8.5zM0 10h12v2H0z" fill="#ccc"/></svg><span>Lorem Ipsum is simply dummy text of the is a printing and typesetting of a now get a1500s, is simply dummy text.</span></li>
  <li><svg width="12" height="12" viewBox="0 0 16 16"><path d="M3 1.5l3 .5 1 3.5-2 1.2a9 9 0 0 0 4.3 4.3l1.2-2 3.5 1 .5 3c-7 1-13-5-11.5-11.5z" fill="#ccc"/></svg><span>00 44 303 555 0142</span></li>
  <li><svg width="12" height="12" viewBox="0 0 12 12"><rect x="3" y="0" width="6" height="3" fill="#ccc"/><rect x="0" y="3.5" width="12" height="5" fill="#ccc"/><rect x="3" y="8" width="6" height="4" fill="#ccc"/></svg><span>00 44 303 555 0142</span></li>
  <li><svg width="12" height="10" viewBox="0 0 12 10"><rect width="12" height="10" fill="#ccc"/><path d="M0 0l6 5 6-5" stroke="#1a1a1a" fill="none"/></svg><span>info@craftwellhub.example</span></li>
</ul>

<ul class="f-posts abs">
  <li><span>Lates Projects</span><span>(12)</span></li>
  <li><span>Blog</span><span>(12)</span></li>
  <li><span>Featured</span><span>(12)</span></li>
  <li><span>News</span><span>(12)</span></li>
  <li><span>Hot Products</span><span>(12)</span></li>
</ul>

<div class="f-photos abs">
  <div class="p1" role="img" aria-label="Builder at work"></div>
  <div class="p2" role="img" aria-label="Site office"></div>
  <div class="p3" role="img" aria-label="Hard hats on a table"></div>
  <div class="p4" role="img" aria-label="Team meeting"></div>
  <div class="p5" role="img" aria-label="Worker in yellow helmet"></div>
  <div class="p6" role="img" aria-label="Trainees on site"></div>
</div>

<form class="f-form abs">
  <div class="field">Name</div>
  <div class="field">Email</div>
  <div class="field msg">Message</div>
  <div class="btn">GET A QUICK QUOTE</div>
</form>

<div class="f-social abs">
  <span style="background:#3b5998"></span><span style="background:#1da1f2"></span><span style="background:#dd4b39"></span><span style="background:#ea4c89"></span><span style="background:#cb2027"></span>
</div>

<div class="f-bottom abs"></div>
<p class="copyright abs">2016 Craftwell Hub, All Right Reserved</p>
<div class="totop abs"><svg width="8" height="8" viewBox="0 0 8 8"><path d="M1 4l3-3 3 3M1 7l3-3 3 3" stroke="#ccc" fill="none"/></svg></div>

</body>
</html>
```